New webpage for Facility Management Company (cleaning services)

We need a new web page design for a company based in Stockholm, Sweden, called TKR Clean AB (established 1991). We provide cleaning services to the public sector, to businesses, and to home owners. Our services primarily include daily cleaning, floor care, window cleaning, and carpet cleaning.

Our company holds certificates for ISO 9001, ISO 14001, ISO 45001 and "Hjorten".

Referring to "the Swedish model" we honor collective agreements between Veltrio (employer-representative organisation and relevant labour unions (e.g. Arbetsfront).
The final design should communicate that we are a trustworthy company with a well trained staff, high quality services combined with a commitment to run a sustainable business from a labour and environmental perspective.

DETAILS
General
-----------------------------------------------
• Language: Swedish (we provide text)
• Very important: Easy to administrate for company staff without special technical skills, especially to
o add/change information about HQ staff
o change any text
o add/change information about offered services
• Responsive
• SEO-friendly

Content that web page needs to cover in one way or the other
--------------------------------------------
• Information about our company
• About our staff and contact info to HQstaff/management (photos, contact info)
• Our ambitions and supporting info (quality, environment, labour conditions, certificates, etc)
• Information to customers within the public sector
• Information to customers within the private sector
• Information to customers within the home owner sector
• Services public sector (Swedish = Offentlig sektor)
• Services private business sector (Swedish = Företag) Se törnvall
• Services home owner sector (Swedish=Privat)
• GDPR compliance
• News

Content/Function
-------------------------------
• One specific requirement is that we need a page for information to potentially new employees (some general information and open job positions) with a possibility to fill in a simple application form and upload CV.(Mail?) CAPTCHA or equivalent.
• Contact form for customers with CAPTCHA or equivalent.
• Cookie management
• Integration social media (future); easy to manage/add/delete integration of social media.

We are not interested in a blog at this point of time

```html
<!DOCTYPE html>
<html lang="en">
<head>
<meta charset="utf-8">
<title>TKR Clean AB – Cleaning services in Stockholm</title>
<link rel="stylesheet" href="https://fonts.googleapis.com/css2?family=Roboto:wght@400;500;700&family=Montserrat:ital,wght@0,400;0,500;1,400&display=swap">
<style>
:root{
  --blue:#0b8ad9;
  --blue-dark:#0670b8;
  --green:#3db44a;
  --green-light:#5fc45a;
  --ink:#1e1e1e;
  --text:#333;
  --muted:#555;
  --footer:#262626;
  --white:#fff;
}
*{margin:0;padding:0;box-sizing:border-box}
html,body{width:1200px;height:4090px;overflow:hidden}
body{font-family:"Roboto",sans-serif;color:var(--text);background:var(--white);position:relative}
.abs{position:absolute}
.brand{display:flex;align-items:center;gap:10px;font-family:"Roboto",sans-serif;font-weight:400;color:var(--ink);white-space:nowrap}
.brand-dot{width:26px;height:26px;border-radius:50%;background:var(--green);flex:none}
.btn{display:inline-flex;align-items:center;justify-content:center;background:var(--blue);color:var(--white);border-radius:30px;font-weight:500;text-decoration:none}

/* top bar */
.topbar{left:0;top:0;width:1200px;height:40px;font-size:13px;font-family:"Montserrat",sans-serif;color:#444}
.lang{left:171px;top:12px;display:flex;gap:6px;align-items:center}
.flag{width:20px;height:13px;background:#2a3f8f;border:1px solid #ccc;position:relative}
.flag::before{content:"";position:absolute;left:0;top:5px;width:100%;height:3px;background:#d22}
.contact-line{right:173px;top:12px;display:flex;gap:10px;align-items:center}
.nav{left:0;top:40px;width:1200px;height:84px;border-bottom:1px solid #eee}
.nav .brand{position:absolute;left:171px;top:24px;font-size:32px}
.menu{position:absolute;right:173px;top:34px;display:flex;gap:19px;font-size:14px;font-weight:500;letter-spacing:.5px;color:#222}

/* hero */
.hero{left:0;top:124px;width:1200px;height:680px;overflow:hidden}
.hero-photo{position:absolute;inset:0;background:linear-gradient(90deg,#f6f6f6 0%,#ececec 35%,#c8c8cc 60%,#9ea3a8 80%,#c3b9ae 100%)}
.hero-copy{position:absolute;left:171px;top:108px;white-space:nowrap}
.hero-copy .kicker{font-family:"Montserrat",sans-serif;font-style:italic;font-size:24px;color:#222}
.hero-copy h1{font-size:54px;font-weight:700;color:var(--green);margin-top:6px}
.hero-copy .sub{font-family:"Montserrat",sans-serif;font-size:21px;color:#222;margin-top:22px}
.hero-copy .name{font-size:56px;font-weight:700;color:#111;margin-top:8px}
.hero-copy .btn{width:162px;height:50px;font-size:21px;margin-top:26px}
.arrow{position:absolute}

/* about */
.about{left:171px;top:880px;width:460px}
.about .eyebrow{font-size:24px;color:#111;padding-left:50px}
.about h2{font-size:36px;font-weight:500;color:var(--blue);padding-left:50px;white-space:nowrap}
.about p{font-size:12.4px;line-height:24px;color:#333;margin-top:22px;text-align:justify}
.about .btn{width:132px;height:40px;font-size:16px;margin-top:22px}
.about-visual{left:680px;top:868px;width:350px;height:330px}

/* services */
.services{left:0;top:1278px;width:1200px;height:630px}
.section-head{position:absolute;width:1200px;left:0;text-align:center}
.section-head .small{font-size:22px}
.section-head .big{font-size:36px;font-weight:500}
.svc{position:absolute;width:215px;color:var(--white)}
.svc h3{font-size:22px;font-weight:500;letter-spacing:.5px;white-space:nowrap}
.svc p{font-size:13px;line-height:20px;margin-top:8px;opacity:.85;text-align:justify;text-align-last:inherit}
.svc.left{text-align:right}
.svc.left p{text-align-last:right}
.center-brand{position:absolute;left:480px;top:1620px;width:240px;text-align:center;font-size:34px;color:var(--ink);white-space:nowrap}

/* ambitions */
.amb-item{position:absolute;text-align:center;width:180px}
.amb-item h4{font-size:20px;font-weight:500;color:#111;margin-top:14px;white-space:nowrap}
.amb-item p{font-size:12.5px;line-height:19px;color:#444;margin-top:8px}
.amb-icon{margin:0 auto;border:2px solid;border-radius:10px;background:#fff;display:flex;align-items:center;justify-content:center}

/* info cards */
.info-card{position:absolute;top:2722px;width:272px;height:240px;border-radius:14px;overflow:hidden}
.info-label{position:absolute;left:0;bottom:0;width:220px;height:64px;background:#fff;border-top-right-radius:60px;padding:14px 0 0 14px}
.info-label b{display:block;font-size:19px;font-weight:500;color:#111}
.info-label span{font-size:16px;color:#222}

/* news */
.news-card{position:absolute;top:3306px;width:413px;height:262px;background:#fff;border-radius:12px;box-shadow:0 4px 18px rgba(0,0,0,.12);overflow:hidden}
.news-card .photo{position:absolute;left:0;top:0;width:198px;height:262px}
.news-body{position:absolute;left:210px;top:20px;width:190px}
.news-body h3{font-size:22px;font-weight:500;color:#111;white-space:nowrap}
.news-body p{font-size:11.6px;line-height:18px;color:#333;margin-top:12px;text-align:justify}
.news-body .btn{width:115px;height:34px;font-size:14px;margin-top:14px}

/* footer */
.footer{left:0;top:3658px;width:1200px;height:432px;background:var(--footer);color:var(--white)}
.footer .brand{position:absolute;left:171px;top:110px;font-size:40px;color:var(--white)}
.footer .brand-dot{background:var(--white);width:30px;height:30px}
.social{position:absolute;left:171px;top:182px;display:flex;gap:14px}
.social span{width:38px;height:38px;border:1.5px solid #fff;border-radius:50%}
.links{position:absolute;left:522px;top:92px}
.links h4,.form h4{font-size:22px;font-weight:500;white-space:nowrap}
.links ul{list-style:none;margin-top:12px;font-size:14px;line-height:24px}
.form{position:absolute;left:688px;top:92px;width:340px}
.field{background:#fff;color:#333;font-size:13px;border-radius:18px;padding:0 12px;display:flex;align-items:center}
.footer .btn{position:absolute;left:690px;top:300px;width:90px;height:36px;font-size:15px}
.rule{position:absolute;left:171px;top:355px;width:857px;height:1px;background:#666}
.copy{position:absolute;left:0;top:395px;width:1200px;text-align:center;font-size:14px;font-weight:500}
</style>
</head>
<body>

<div class="abs topbar">
  <div class="abs lang"><span class="flag"></span> Eng ▾</div>
  <div class="abs contact-line">
    <svg width="14" height="16" viewBox="0 0 14 16"><path d="M7 1a5 5 0 0 0-5 5c0 4 5 9 5 9s5-5 5-9a5 5 0 0 0-5-5z" fill="none" stroke="#333" stroke-width="1.5"/><circle cx="7" cy="6" r="1.8" fill="#333"/></svg>
    <span>18 Lindgatan, Stockholm, Sweden</span>
    <svg width="14" height="14" viewBox="0 0 14 14"><path d="M3 1l3 3-2 2a8 8 0 0 0 4 4l2-2 3 3-2 2C6 13 1 8 1 3z" fill="none" stroke="#333" stroke-width="1.5"/></svg>
    <span>0812345678</span>
  </div>
</div>

<header class="abs nav">
  <div class="brand"><span class="brand-dot"></span>TKR Clean AB</div>
  <nav class="menu"><span>HOME</span><span>ABOUT</span><span>SERVICES</span><span>PRICING</span><span>BLOG</span><span>CONTACT</span></nav>
</header>

<section class="abs hero">
  <div class="hero-photo" role="img" aria-label="Tired young cleaner in yellow gloves sitting by a sofa with mop, bucket and cleaning products"></div>
  <svg class="abs" style="left:0;bottom:0" width="1200" height="140" viewBox="0 0 1200 140" preserveAspectRatio="none">
    <path d="M0 120 Q30 70 70 110 Q110 60 160 100 Q220 55 280 90 Q300 20 380 40 Q440 0 500 45 Q560 20 620 60 Q680 40 720 80 Q780 30 860 70 Q900 90 960 110 Q1020 60 1080 90 Q1140 70 1200 100 L1200 140 L0 140Z" fill="#fff"/>
  </svg>
  <div class="hero-copy">
    <div class="kicker">'Tired' of all these</div>
    <h1>Cleaning?</h1>
    <div class="sub">Get connected with us</div>
    <div class="name">TKR Clean AB</div>
    <a class="btn">Contact Us</a>
  </div>
  <svg class="arrow" style="left:54px;top:276px" width="30" height="70"><path d="M26 2 L4 35 L26 68" fill="none" stroke="#444" stroke-width="2"/></svg>
  <svg class="arrow" style="left:1106px;top:276px" width="30" height="70"><path d="M4 2 L26 35 L4 68" fill="none" stroke="#eee" stroke-width="2"/></svg>
</section>

<section class="abs about">
  <div class="eyebrow">About</div>
  <h2>TKR Clean AB</h2>
  <p>Nemo enim ipsam voluptatem quia voluptas sit aspernatur aut odit aut fugit, sed quia consequuntur magni dolores eos qui ratione voluptatem sequi nesciunt. Neque porro quisquam est, qui dolorem ipsum quia dolor sit amet, consectetur, adipisci velit, sed quia non numquam eius modi tempora incidunt ut labore et dolore magnam aliquam quaerat voluptatem. Ut enim ad minima veniam, quis nostrum exercitationem ullam corporis suscipit laboriosam.</p>
  <a class="btn">Read More</a>
</section>
<div class="abs about-visual">
  <svg width="350" height="330" viewBox="0 0 350 330">
    <circle cx="175" cy="165" r="162" fill="#fff" stroke="#e2e2e2" stroke-width="4"/>
    <defs><clipPath id="aboutClip"><circle cx="175" cy="165" r="150"/></clipPath>
      <linearGradient id="aboutGrad" x1="0" x2="1"><stop offset="0" stop-color="#9fb5c4"/><stop offset=".5" stop-color="#d9e4ea"/><stop offset="1" stop-color="#5aa7d6"/></linearGradient></defs>
    <rect x="25" y="15" width="300" height="300" fill="url(#aboutGrad)" clip-path="url(#aboutClip)" role="img" aria-label="Smiling cleaner in blue apron spraying a window"/>
    <g fill="#fff" stroke="#d5d5d5" stroke-width="3">
      <circle cx="50" cy="65" r="42"/><circle cx="300" cy="65" r="42"/>
      <circle cx="50" cy="245" r="42"/><circle cx="300" cy="245" r="42"/>
    </g>
    <g fill="none" stroke="#222" stroke-width="2">
      <rect x="36" y="50" width="28" height="30" rx="4"/><line x1="36" y1="62" x2="64" y2="62"/>
      <path d="M285 85 h30 v-20 h-30z M300 65 v-20"/>
      <path d="M30 260 l20-22 20 22 M36 256 v16 h28 v-16"/>
      <path d="M288 258 l14-28 10 6 -10 26z"/>
    </g>
  </svg>
</div>

<section class="abs services">
  <svg width="1200" height="630" viewBox="0 0 1200 630" preserveAspectRatio="none">
    <defs><linearGradient id="svcGrad" x1="0" y1="0" x2="0" y2="1"><stop offset="0" stop-color="#1a93e0"/><stop offset="1" stop-color="#0b7fcf"/></linearGradient></defs>
    <path d="M0 45 Q600 -40 1200 45 L1200 585 Q600 670 0 585Z" fill="url(#svcGrad)" role="img" aria-label="Blue band over a faint photo of cleaning equipment"/>
    <g fill="none" stroke="#fff" stroke-width="2">
      <path d="M405 257 h55 l55 40"/><path d="M795 257 h-55 l-55 40"/>
      <path d="M405 484 h55 l55-40"/><path d="M795 484 h-55 l-55-40"/>
    </g>
    <circle cx="600" cy="365" r="135" fill="#0a70b6"/>
    <circle cx="600" cy="365" r="122" fill="none" stroke="#fff" stroke-width="4"/>
    <circle cx="600" cy="365" r="112" fill="#fff"/>
  </svg>
  <div class="section-head" style="top:70px;color:#fff"><div class="small">Our</div><div class="big">TKR Clean AB Services</div></div>
  <div class="svc left" style="left:175px;top:242px"><h3>DAILY CLEANING</h3><p>Duis aute irure dolor in reprehender it in voluptate velit esse cillum dolorem</p></div>
  <div class="svc" style="left:805px;top:242px"><h3>WINDOW CLEANING</h3><p>Duis aute irure dolor in reprehender it in voluptate velit esse cillum dolorem</p></div>
  <div class="svc left" style="left:175px;top:438px"><h3>FLOOR CARE</h3><p>Duis aute irure dolor in reprehender it in voluptate velit esse cillum dolorem</p></div>
  <div class="svc" style="left:805px;top:438px"><h3>CARPET CLEANING</h3><p>Duis aute irure dolor in reprehender it in voluptate velit esse cillum dolorem</p></div>
</section>
<div class="center-brand">TKR Clean AB</div>

<div class="section-head" style="top:2026px"><div class="small" style="color:#111">Our Ambitions</div><div class="big" style="color:var(--blue)">Supporting Info</div></div>
<svg class="abs" style="left:250px;top:2190px" width="720" height="90"><path d="M50 70 Q110 90 170 20 M240 20 Q310 90 380 60 M450 60 Q520 80 580 20" fill="none" stroke="#999" stroke-width="1.5" stroke-dasharray="5 5"/></svg>
<div class="amb-item" style="left:160px;top:2208px">
  <div class="amb-icon" style="width:88px;height:88px;border-color:var(--blue)"><svg width="46" height="46"><circle cx="23" cy="20" r="15" fill="none" stroke="var(--blue)" stroke-width="2"/><path d="M15 33 l-4 12 12-5 12 5-4-12" fill="none" stroke="var(--blue)" stroke-width="2"/></svg></div>
  <h4>Quality</h4><p>Duis aute irure dolor in repr ehenderit in voluptate velit esse cillum dolore</p></div>
<div class="amb-item" style="left:385px;top:2162px">
  <div class="amb-icon" style="width:102px;height:102px;border-color:var(--green)"><svg width="54" height="54"><path d="M4 38 h14 l14 6 18-10 M27 28 v-16 M27 14 c-8 0-10-6-10-10 8 0 10 6 10 10z M27 14 c8 0 10-6 10-10-8 0-10 6-10 10z" fill="none" stroke="var(--green)" stroke-width="2"/></svg></div>
  <h4>Environment</h4><p>Duis aute irure dolor in repr ehenderit in voluptate velit esse cillum dolore</p></div>
<div class="amb-item" style="left:625px;top:2208px">
  <div class="amb-icon" style="width:88px;height:88px;border-color:var(--blue)"><svg width="46" height="46"><circle cx="23" cy="16" r="9" fill="none" stroke="var(--blue)" stroke-width="2"/><path d="M6 44 c0-12 8-16 17-16 s17 4 17 16z" fill="none" stroke="var(--blue)" stroke-width="2"/></svg></div>
  <h4>Labour Conditions</h4><p>Duis aute irure dolor in repr ehenderit in voluptate velit esse cillum dolore</p></div>
<div class="amb-item" style="left:857px;top:2162px">
  <div class="amb-icon" style="width:102px;height:102px;border-color:var(--green)"><svg width="50" height="54"><rect x="6" y="4" width="32" height="42" rx="3" fill="none" stroke="var(--green)" stroke-width="2"/><path d="M12 14 h20 M12 21 h20 M12 28 h12" stroke="var(--green)" stroke-width="2"/><circle cx="38" cy="40" r="8" fill="#fff" stroke="var(--green)" stroke-width="2"/></svg></div>
  <h4>Certificates</h4><p>Duis aute irure dolor in repr ehenderit in voluptate velit esse cillum dolore</p></div>

<svg class="abs" style="left:0;top:2476px" width="1200" height="600" viewBox="0 0 1200 600" preserveAspectRatio="none">
  <defs><linearGradient id="infoGrad" x1="0" y1="0" x2="0" y2="1"><stop offset="0" stop-color="#5cc35a"/><stop offset="1" stop-color="#37ae44"/></linearGradient></defs>
  <path d="M0 45 Q600 -40 1200 45 L1200 550 Q600 640 0 550Z" fill="url(#infoGrad)" role="img" aria-label="Green band over a faint photo of cleaning equipment"/>
</svg>
<div class="section-head" style="top:2596px;color:#fff"><div class="small">Our</div><div class="big">TKR Clean AB Information</div></div>
<svg class="abs" style="left:54px;top:2740px" width="30" height="70"><path d="M26 2 L4 35 L26 68" fill="none" stroke="#fff" stroke-width="2"/></svg>
<svg class="abs" style="left:1106px;top:2740px" width="30" height="70"><path d="M4 2 L26 35 L4 68" fill="none" stroke="#fff" stroke-width="2"/></svg>

<div class="info-card" style="left:171px">
  <div style="position:absolute;inset:0;background:linear-gradient(135deg,#8d8d8d,#3e3e3e 60%,#5d6b58)" role="img" aria-label="Cleaner vacuuming a sofa in an office"></div>
  <div class="info-label"><b>Customers Info</b><span>Public Sector</span></div>
</div>
<div class="info-card" style="left:463px">
  <div style="position:absolute;inset:0;background:linear-gradient(135deg,#e4e4e4,#8a8f96 55%,#1d3a66)" role="img" aria-label="Cleaner in yellow gloves wiping an office shelf"></div>
  <div class="info-label"><b>Customers Info</b><span>Private Sector</span></div>
</div>
<div class="info-card" style="left:755px">
  <div style="position:absolute;inset:0;background:linear-gradient(135deg,#f2f2f2,#c9c9c9 55%,#3b3b3b)" role="img" aria-label="Cleaner dusting a computer desk at home"></div>
  <div class="info-label"><b>Customers Info</b><span>Home Owner Sector</span></div>
</div>

<div class="section-head" style="top:3184px"><div class="small" style="color:#111">Our</div><div class="big" style="color:var(--blue)">Latest News</div></div>

<article class="news-card" style="left:171px">
  <div class="photo" style="background:linear-gradient(160deg,#e9e6e0,#2c8fa8 55%,#b99770)" role="img" aria-label="Cleaner in teal shirt and yellow gloves wiping a counter"></div>
  <div class="news-body"><h3>Duis aute irure</h3>
    <p>Lorem ipsum dolor sit amet, consectetur adipiscing elit, sed do eiusmod tempor incididunt ut labore. Duis aute irure dolor in reprehenderit in voluptate velit esse cillum. Non proident, sunt in culpa qui officia deserunt mollit anim id est laborum.</p>
    <a class="btn">Read More</a></div>
</article>
<article class="news-card" style="left:614px">
  <div class="photo" style="background:linear-gradient(160deg,#e8ecef,#8a9aad 50%,#6e4b33)" role="img" aria-label="Cleaner mopping an office floor"></div>
  <div class="news-body"><h3>Duis aute irure</h3>
    <p>Lorem ipsum dolor sit amet, consectetur adipiscing elit, sed do eiusmod tempor incididunt ut labore. Duis aute irure dolor in reprehenderit in voluptate velit esse cillum. Non proident, sunt in culpa qui officia deserunt mollit anim id est laborum.</p>
    <a class="btn">Read More</a></div>
</article>

<footer class="abs footer">
  <div class="brand"><span class="brand-dot"></span>TKR Clean AB</div>
  <div class="social"><span></span><span></span><span></span></div>
  <div class="links"><h4>Quick Links</h4>
    <ul><li>Home</li><li>About</li><li>Services</li><li>Pricing</li><li>Blog</li><li>Contact</li></ul></div>
  <div class="form"><h4>Contact Form</h4>
    <div style="display:flex;gap:8px;margin-top:20px">
      <div class="field" style="width:166px;height:36px">Name</div>
      <div class="field" style="width:166px;height:36px">Email</div>
    </div>
    <div class="field" style="width:340px;height:74px;margin-top:10px;align-items:flex-start;padding-top:10px;border-radius:12px">Message</div>
  </div>
  <a class="btn">Submit</a>
  <div class="rule"></div>
  <div class="copy">Copyrights @ 2022 TKR Clean AB</div>
</footer>

</body>
</html>
```